Tidewell Recovery Business Card Design

Professional and clean design. The design colors should flow with the logo. Two-sided card with the website on the back which is:

www.TidewellRecovery.example.

"Specializing in Water Damage Restoration"

On the front I need the name, email, phone, and logo.

Name: Dorian Vashti
Email: Dorian@TidewellRecovery.example
Phone: 555-318-2046 for now

I only have the Preview and Thumbnail right now but should have the source files uploaded within a day or two.

Target Market(s)

Flood victims, home owners with water damage from busted pipes etc...

Industry/Entity Type

Business

Contact Information for Business Card

Name: Dorian Vashti

Font styles to use
Serif
Sans Serif

```html
<!DOCTYPE html>
<html lang="en">
<head>
<meta charset="utf-8">
<title>Tidewell Recovery Business Card</title>
<link rel="stylesheet" href="https://fonts.googleapis.com/css2?family=EB+Garamond:wght@400;600;700&display=swap">
<style>
  :root {
    --backdrop: #262626;
    --card-white: #f7f7f7;
    --card-black: #161616;
    --brand-blue: #4fb0de;
    --brand-deep: #2b87bf;
    --mark-blue: #1d3a4d;
    --ink-dark: #333333;
    --ink-light: #c9c9c9;
  }
  html, body {
    margin: 0;
    width: 1200px;
    height: 900px;
    overflow: hidden;
    background: var(--backdrop);
    font-family: "EB Garamond", Georgia, serif;
  }
  .canvas {
    position: relative;
    width: 1200px;
    height: 900px;
  }
  .card {
    position: absolute;
    left: 340px;
    width: 520px;
    height: 297px;
    box-sizing: border-box;
    overflow: hidden;
    box-shadow: 0 10px 30px rgba(0,0,0,0.5);
  }
  /* Front */
  .card-front {
    top: 120px;
    background: var(--card-white);
  }
  .brand-lockup {
    position: absolute;
    left: 34px;
    top: 40px;
    display: flex;
    align-items: center;
    gap: 12px;
  }
  .brand-dot {
    width: 30px;
    height: 30px;
    border-radius: 50%;
    background: var(--brand-blue);
  }
  .brand-name {
    font-size: 22px;
    font-weight: 600;
    letter-spacing: 3px;
    text-transform: uppercase;
    color: var(--brand-blue);
    line-height: 1;
  }
  .person {
    position: absolute;
    right: 30px;
    top: 118px;
    display: flex;
    align-items: baseline;
    gap: 14px;
  }
  .person-name {
    font-size: 21px;
    font-weight: 600;
    color: var(--brand-blue);
  }
  .person-title {
    font-size: 13px;
    color: var(--ink-dark);
  }
  .divider {
    position: absolute;
    left: 34px;
    right: 30px;
    top: 152px;
    height: 2px;
    background: var(--brand-blue);
  }
  .contacts {
    position: absolute;
    left: 34px;
    top: 176px;
    margin: 0;
    padding: 0;
    list-style: none;
    font-size: 15px;
    color: var(--ink-dark);
    line-height: 1.6;
  }
  .contacts li {
    display: flex;
    align-items: center;
    gap: 10px;
  }
  .contacts svg { width: 13px; height: 13px; fill: var(--brand-blue); }
  /* Back */
  .card-back {
    top: 483px;
    background: var(--card-black);
  }
  .back-mark {
    position: absolute;
    left: 22px;
    top: 42px;
    width: 210px;
    height: 210px;
    border-radius: 50%;
    background: var(--mark-blue);
  }
  .back-copy {
    position: absolute;
    right: 28px;
    top: 110px;
    text-align: right;
  }
  .back-brand {
    font-size: 28px;
    font-weight: 600;
    letter-spacing: 4px;
    text-transform: uppercase;
    color: var(--brand-deep);
    line-height: 1.1;
    margin: 0 0 14px;
  }
  .tagline {
    font-size: 18px;
    color: var(--ink-light);
    margin: 0 0 4px;
  }
  .website {
    font-size: 17px;
    font-weight: 700;
    color: var(--ink-light);
    margin: 0;
  }
</style>
</head>
<body>
<main class="canvas">
  <section class="card card-front" aria-label="Card front">
    <div class="brand-lockup">
      <span class="brand-dot"></span>
      <span class="brand-name">Tidewell Recovery</span>
    </div>
    <div class="person">
      <span class="person-name">Dorian Vashti</span>
      <span class="person-title">Director/Owner</span>
    </div>
    <div class="divider"></div>
    <ul class="contacts">
      <li>
        <svg viewBox="0 0 24 24" aria-hidden="true"><path d="M6.6 10.8a15.1 15.1 0 0 0 6.6 6.6l2.2-2.2a1 1 0 0 1 1-.25 11.4 11.4 0 0 0 3.6.57 1 1 0 0 1 1 1V20a1 1 0 0 1-1 1A17 17 0 0 1 3 4a1 1 0 0 1 1-1h3.5a1 1 0 0 1 1 1c0 1.25.2 2.45.57 3.57a1 1 0 0 1-.25 1z"/></svg>
        555-318-2046
      </li>
      <li>
        <svg viewBox="0 0 24 24" aria-hidden="true"><path d="M2 5h20v14H2z M2 5l10 8 10-8" fill="none" stroke="#4fb0de" stroke-width="2"/></svg>
        Dorian@TidewellRecovery.example
      </li>
    </ul>
  </section>

  <section class="card card-back" aria-label="Card back">
    <div class="back-mark"></div>
    <div class="back-copy">
      <p class="back-brand">Tidewell Recovery</p>
      <p class="tagline">Specializing in Water Damage Restoration</p>
      <p class="website">www.TidewellRecovery.example</p>
    </div>
  </section>
</main>
</body>
</html>
```